Flyer for local business that installs fences and sells fence materials

We recently began selling fence materials, in addition to also doing fence installations. We need a flyer that displays our business information and photos of our work, as well as a flyer that shows customers they have the option to buy materials only also.

If they are looking to build a fence - we can help by installing it, or if they want to install themselves, they can buy the materials only from us too. We provide a lifetime warranty on all materials and installations. More information about the company is here: www.BrambleRailWorks.com

Its important to have the company logo, phone number, email and business hours listed (Monday - Thursday 9AM - 3PM, Friday 9AM - 1PM).

It is also important to show the fence material types we offer:
Wood, Chainlink, Vinyl and Aluminum
Updates

Updated with more photos and url to website www.bramblerailworks.com for details

Target Market(s)

Residential Homeowners

Industry/Entity Type

Construction

Font styles to use
Sans Serif
Other font styles liked:
• Arial

Colors
0054AA
0677BA
7BADD7
CADEEF
E8F1F8

Requirements
Must have
• Photos of the fencing we offer
Nice to have
• A way to explain to customers they can hire us to install, or just buy the materials from us
Should not have
• Too many colors or too many words

```html
<!DOCTYPE html>
<html lang="en">
<head>
<meta charset="utf-8">
<title>Bramble Rail Works – We Build Fences Flyer</title>
<link href="https://fonts.googleapis.com/css2?family=Graduate&family=Poppins:wght@400;500;600;700;800&display=swap" rel="stylesheet">
<style>
  :root{
    --orange:#E8912F;
    --orange-dark:#C9701A;
    --brown:#5A3D2B;
    --brown-dark:#4A3122;
    --blue:#2E7DC6;
    --blue-btn:#3B86D0;
    --ink:#2B2B2B;
    --white:#FFFFFF;
  }
  *{box-sizing:border-box;margin:0;padding:0}
  html,body{width:865px;height:1200px;overflow:hidden;background:#fff}
  .flyer{position:relative;width:865px;height:1200px;background:var(--white);font-family:"Poppins",Arial,sans-serif;color:var(--ink)}

  /* left column */
  .brand{position:absolute;left:52px;top:58px;display:flex;align-items:center;gap:12px}
  .brand-mark{width:14px;height:14px;border-radius:50%;background:var(--orange);align-self:flex-start;margin-top:6px}
  .brand-name{font-weight:700;font-size:24px;color:var(--blue);line-height:1.05}
  .brand-phone{font-weight:700;font-size:22px;color:var(--ink);line-height:1.15}
  .brand-tag{font-weight:600;font-size:7.5px;color:var(--ink);letter-spacing:.1px}

  .headline{position:absolute;left:50px;top:172px;font-family:"Graduate",Georgia,serif;line-height:1.02}
  .headline .line-1{display:block;font-size:66px;color:var(--orange)}
  .headline .line-2{display:block;font-size:66px;color:var(--brown)}

  .subhead{position:absolute;left:52px;top:335px;border-left:5px solid var(--orange);padding-left:12px;font-weight:700;font-size:24px;line-height:1.17;color:var(--ink)}
  .intro{position:absolute;left:52px;top:405px;width:370px;font-weight:500;font-size:17px;line-height:1.23}

  .band{position:absolute;left:0;top:513px;width:452px;height:118px;background:var(--brown);padding:16px 0 0 52px;box-shadow:0 8px 10px -6px rgba(0,0,0,.3)}
  .band-title{font-weight:700;font-size:25px;line-height:1.15;color:var(--white)}
  .band-note{font-weight:500;font-size:12px;color:var(--orange);margin-top:2px}

  .features{position:absolute;left:54px;top:668px;list-style:none}
  .features li{display:flex;align-items:flex-start;gap:8px;font-size:17px;line-height:1.2;height:32.5px}
  .features li svg{flex:0 0 18px;margin-top:2px}

  .virtual-title{position:absolute;left:50px;top:970px;font-weight:700;font-size:19.5px;line-height:1.1;color:var(--blue)}
  .virtual-note{position:absolute;left:50px;top:1030px;font-weight:700;font-size:17px}
  .big-phone{position:absolute;left:50px;top:1044px;display:flex;align-items:center;gap:6px;font-weight:800;font-size:42px;color:var(--ink)}
  .hours{position:absolute;left:52px;top:1106px;font-size:17px;line-height:1.25}
  .hours b{color:var(--orange-dark);font-weight:700}

  /* right column */
  .gallery{position:absolute;left:440px;top:0;width:425px;height:1200px;background:var(--orange)}
  .photo{position:absolute}
  .photo-main{left:8px;top:8px;width:417px;height:561px;background:linear-gradient(180deg,#9DB4C9 0%,#3F5A2E 30%,#6E7D3A 52%,#C7A46A 62%,#5E7A34 80%,#6A4226 100%)}
  .photo-wood{left:8px;top:577px;width:207px;height:221px;background:linear-gradient(180deg,#B9C6D2 0%,#D8C3A0 25%,#CDB48C 80%,#6E7F3A 100%)}
  .photo-aluminum{left:223px;top:577px;width:202px;height:221px;background:linear-gradient(180deg,#DDE6EC 0%,#5B7A3E 40%,#2E2E2E 55%,#6F9A3F 100%)}
  .photo-vinyl{left:8px;top:806px;width:207px;height:221px;background:linear-gradient(180deg,#3E6FD1 0%,#8FAEE8 30%,#F2F2F2 45%,#E8E8E8 92%,#A44A2C 100%)}
  .photo-chain{left:223px;top:806px;width:202px;height:221px;background:linear-gradient(180deg,#B9CDE2 0%,#5C7440 35%,#8FA760 60%,#6F8C3B 100%)}
  .photo-label{position:absolute;left:50%;bottom:12px;transform:translateX(-50%);background:var(--blue-btn);color:var(--white);font-weight:600;font-size:12.5px;padding:6px 0;width:142px;text-align:center;white-space:nowrap}

  .cta{position:absolute;left:0;top:1048px;width:425px;text-align:center;font-weight:700;font-size:23px;color:var(--white)}
  .cta span{color:#FFE7C4}
  .url-pill{position:absolute;left:36px;top:1087px;width:368px;height:30px;border-radius:15px;background:var(--orange-dark);color:var(--white);text-align:center;font-size:17px;line-height:30px;letter-spacing:1.4px}
  .url-pill b{font-weight:700}
  .contact{position:absolute;left:36px;top:1123px;width:380px;display:flex;justify-content:space-between;font-size:11.5px;font-weight:500;color:var(--white);line-height:1.2}
  .contact div{display:flex;gap:4px;align-items:flex-start}
</style>
</head>
<body>
<div class="flyer">

  <header class="brand">
    <span class="brand-mark"></span>
    <div>
      <div class="brand-name">Bramble Rail Works</div>
      <div class="brand-phone">555-014-2290</div>
      <div class="brand-tag">"Because Good Fences Make Good Neighbors"</div>
    </div>
  </header>

  <h1 class="headline"><span class="line-1">WE BUILD</span><span class="line-2">FENCES</span></h1>

  <p class="subhead">We will love to build your<br>fence too</p>
  <p class="intro">We strive to provide our customers with the best fence experience possible. We want your fence installation process to go smoothly and easily, from start to finish.</p>

  <section class="band">
    <div class="band-title">BEAUTIFUL, PROFESSIONALL<br>INSTALLED FENCES</div>
    <div class="band-note">AT AFFORDABLE PRICES! MANY FENCE STYLES AVALLABLE.</div>
  </section>

  <ul class="features">
    <li><svg width="18" height="18" viewBox="0 0 18 18"><circle cx="9" cy="9" r="9" fill="#E8912F"/><path d="M5 9.3l2.7 2.6L13 6.5" stroke="#fff" stroke-width="2.2" fill="none" stroke-linecap="round" stroke-linejoin="round"/></svg>Free Estimates</li>
    <li><svg width="18" height="18" viewBox="0 0 18 18"><circle cx="9" cy="9" r="9" fill="#E8912F"/><path d="M5 9.3l2.7 2.6L13 6.5" stroke="#fff" stroke-width="2.2" fill="none" stroke-linecap="round" stroke-linejoin="round"/></svg>Professional Installation</li>
    <li><svg width="18" height="18" viewBox="0 0 18 18"><circle cx="9" cy="9" r="9" fill="#E8912F"/><path d="M5 9.3l2.7 2.6L13 6.5" stroke="#fff" stroke-width="2.2" fill="none" stroke-linecap="round" stroke-linejoin="round"/></svg>Concrete In EVERY Post</li>
    <li><svg width="18" height="18" viewBox="0 0 18 18"><circle cx="9" cy="9" r="9" fill="#E8912F"/><path d="M5 9.3l2.7 2.6L13 6.5" stroke="#fff" stroke-width="2.2" fill="none" stroke-linecap="round" stroke-linejoin="round"/></svg>HOA Submission Assistance</li>
    <li><svg width="18" height="18" viewBox="0 0 18 18"><circle cx="9" cy="9" r="9" fill="#E8912F"/><path d="M5 9.3l2.7 2.6L13 6.5" stroke="#fff" stroke-width="2.2" fill="none" stroke-linecap="round" stroke-linejoin="round"/></svg>Lifetime Workmanship Warranty</li>
    <li><svg width="18" height="18" viewBox="0 0 18 18"><circle cx="9" cy="9" r="9" fill="#E8912F"/><path d="M5 9.3l2.7 2.6L13 6.5" stroke="#fff" stroke-width="2.2" fill="none" stroke-linecap="round" stroke-linejoin="round"/></svg>Experienced Installation Teams</li>
    <li><svg width="18" height="18" viewBox="0 0 18 18"><circle cx="9" cy="9" r="9" fill="#E8912F"/><path d="M5 9.3l2.7 2.6L13 6.5" stroke="#fff" stroke-width="2.2" fill="none" stroke-linecap="round" stroke-linejoin="round"/></svg>Quality Workmanship &amp; Materials</li>
    <li><svg width="18" height="18" viewBox="0 0 18 18"><circle cx="9" cy="9" r="9" fill="#E8912F"/><path d="M5 9.3l2.7 2.6L13 6.5" stroke="#fff" stroke-width="2.2" fill="none" stroke-linecap="round" stroke-linejoin="round"/></svg><span>FREE Gate Adjustments for LIFE Some<br>restrictions apply</span></li>
  </ul>

  <p class="virtual-title">IF YOU KNOW YOUR MEASUREMENTS<br>OR HAVE A LOT SURVEY,</p>
  <p class="virtual-note">Email or call us for a virtual estimate!</p>
  <div class="big-phone">
    <svg width="34" height="34" viewBox="0 0 34 34"><circle cx="17" cy="17" r="15" fill="none" stroke="#2E7DC6" stroke-width="3"/><path d="M11 10c1-1 2.5-1 3 0l1.5 3c.4.8 0 1.6-.6 2l-1 .8c1 2 2.5 3.5 4.4 4.4l.8-1c.5-.6 1.3-1 2-.6l3 1.5c1 .5 1 2 0 3-2 2-4.5 2-7 .6-3-1.7-5.3-4-7-7-1.3-2.6-1.3-5 .9-6.7z" fill="#2E7DC6"/></svg>
    555-014-2290
  </div>
  <p class="hours">Monday- Thursday: &nbsp;<b>9am - 3pm</b><br>Friday: &nbsp;<b>9am - 1pm</b></p>

  <section class="gallery">
    <div class="photo photo-main" role="img" aria-label="Photo of a stained wooden fence post with an iron bell, overlooking a scalloped wood picket fence and green lawn"></div>
    <div class="photo photo-wood" role="img" aria-label="Photo of a new natural wood privacy fence with gate"><span class="photo-label">WOOD FENCE</span></div>
    <div class="photo photo-aluminum" role="img" aria-label="Photo of a black aluminum fence around a backyard"><span class="photo-label">ALUMINUM FENCE</span></div>
    <div class="photo photo-vinyl" role="img" aria-label="Photo of a white vinyl privacy fence with lattice top under blue sky"><span class="photo-label">VINYL FENCE</span></div>
    <div class="photo photo-chain" role="img" aria-label="Photo of a chain link fence along a grassy yard"><span class="photo-label">CHAIN LINK FENCE</span></div>

    <p class="cta">CALL US FOR A <span>FREE ESTIMATES</span></p>
    <div class="url-pill">www.<b>bramblerailworks</b>.com</div>
    <div class="contact">
      <div><svg width="10" height="13" viewBox="0 0 10 13"><path d="M5 0a5 5 0 0 1 5 5c0 3.5-5 8-5 8S0 8.5 0 5a5 5 0 0 1 5-5z" fill="#fff"/><circle cx="5" cy="5" r="2" fill="#E8912F"/></svg><span>48 Larkspur Ln, Millbrook<br>NC 27000</span></div>
      <div><svg width="12" height="9" viewBox="0 0 12 9" style="margin-top:2px"><rect x=".5" y=".5" width="11" height="8" fill="none" stroke="#fff"/><path d="M.5.5L6 5l5.5-4.5" fill="none" stroke="#fff"/></svg><span>office@bramblerailworks.com</span></div>
    </div>
  </section>

</div>
</body>
</html>
```